Website for business consultancy - bright and happy feel needed

I need a website with 3/4 pages. I want the first page designed first and the rest will be easy. I need some pictures but none with corporate looking people. I need links to chatterbox and careerweb. I need a contact form. I have samples of websites i like, fonts i like and I need a small logo also. I like simple, clean lines and I want a bright, happy and feminine feel. My audience are small businesses so I don't want them intimidated by new much of a corporate feel.
Updates

Project Deadline Extended Reason: I have not received a design that reflects what I believe the brief to be, therefore I am extending the deadline and increasing the amount to be paid. Added Thursday, October 13, 2016

Target Market(s)

Small medium size businesses who want to grow and need that help but they cannot afford a full time financial director.

Industry/Entity Type

Business Consultant

Number of Pages Required

4 page

Font styles to use
Other font styles liked:
• i can attach images

Colors
fcf0f6
e667a6
85cae6
ffffff
fbee3e

Requirements
Must have
• Link to chatterbox and career web
• Contact form linked to my email
• Pictures - full width images where required
• Colour
• Mobile ready
• Soft feminine feel to it
• I dont want it to look like a corporate business consultancy - much more marketing or interior deign feel
Nice to have
• I would like the 3 services I have in 3 boxes that you click and takes you to a place with more information on the service.
• pictures thinking outside of the box
• Can be wordpress if need be
Should not have
• pictures with too much of a corporate feel
• No pictures of coporate people at all
• i like the following websites
• www.pebblordo.co.uk and others that are attached in the documents with a feminine feel to them

```html
<!DOCTYPE html>
<html lang="en">
<head>
<meta charset="utf-8">
<title>maren holt – Business Consultancy</title>
<link rel="stylesheet" href="https://fonts.googleapis.com/css2?family=Kurale&family=Raleway:ital,wght@0,400;0,500;0,700;0,800;1,400&display=swap">
<style>
  :root {
    --white: #ffffff;
    --blush: #fcf0f6;
    --rose: #e667a6;
    --rose-deep: #c94d8b;
    --sky: #85cae6;
    --sky-deep: #4fa9cf;
    --sunshine: #fbee3e;
    --ink: #3a3a3a;
    --nav-ink: #555555;
    --field-border: #e3b9cf;
    --field-fill: #fdf6fa;
    --placeholder: #a88a99;
    --card-marketing: rgba(230, 103, 166, 0.94);
    --card-finance: rgba(79, 169, 207, 0.94);
    --card-coach: rgba(244, 214, 40, 0.96);
  }
  * { box-sizing: border-box; margin: 0; padding: 0; }
  html, body { width: 1200px; height: 800px; overflow: hidden; background: var(--white); }
  body { font-family: "Raleway", Arial, sans-serif; color: var(--ink); }

  .page { position: relative; width: 1200px; height: 800px; overflow: hidden; }

  /* Header */
  .brand {
    position: absolute; left: 135px; top: 12px;
    font-family: "Kurale", Georgia, serif; font-size: 45px; line-height: 50px;
    color: var(--ink); letter-spacing: 0.8px;
  }
  .help-line {
    position: absolute; left: 969px; top: 14px;
    font-size: 10px; color: var(--nav-ink); letter-spacing: 0.6px;
  }
  .main-nav { position: absolute; left: 0; top: 69px; width: 1200px; height: 14px; }
  .main-nav a {
    position: absolute; transform: translateX(-50%);
    font-size: 10.5px; color: var(--nav-ink); text-decoration: none; letter-spacing: 0.2px;
  }
  .accent-band {
    position: absolute; left: 0; top: 89px; width: 1200px; height: 15px;
    background: var(--rose); border-top: 2px solid var(--sunshine);
  }

  /* Hero */
  .hero-photo {
    position: absolute; left: 0; top: 104px; width: 1200px; height: 427px;
    background:
      radial-gradient(ellipse at 78% 30%, var(--blush) 0%, rgba(252, 240, 246, 0) 45%),
      radial-gradient(ellipse at 95% 95%, var(--sky) 0%, rgba(133, 202, 230, 0) 40%),
      linear-gradient(115deg, var(--rose-deep) 0%, var(--rose) 40%, #f0a3c8 65%, #f7cfe1 100%);
  }
  .hero-title {
    position: absolute; left: 213px; top: 256px;
    font-size: 42px; font-weight: 700; line-height: 47px; color: var(--white);
    letter-spacing: 0.3px; text-transform: uppercase;
  }
  .hero-button {
    position: absolute; left: 213px; top: 372px; width: 187px; height: 40px;
    border: 2px solid var(--white); border-radius: 2px;
    display: flex; align-items: center; justify-content: center;
    font-size: 13px; color: var(--white); text-decoration: none; letter-spacing: 0.5px;
  }

  .hero-fade {
    position: absolute; left: 0; top: 531px; width: 1200px; height: 90px;
    background: linear-gradient(to bottom, #ffffff 0%, #ffffff 55%, var(--blush) 85%, #ffffff 100%);
  }

  /* Service cards */
  .service-card {
    position: absolute; top: 493px; width: 300px; height: 137px; padding: 10px;
    text-decoration: none; color: var(--white);
  }
  .service-card--marketing { left: 136px; background: var(--card-marketing); }
  .service-card--finance { left: 453px; background: var(--card-finance); }
  .service-card--coach { left: 769px; background: var(--card-coach); color: var(--ink); }
  .service-card__frame {
    width: 100%; height: 100%; border: 2px solid var(--white);
    text-align: center; padding-top: 20px;
  }
  .service-card__title { font-size: 13px; font-weight: 800; letter-spacing: 0.3px; text-transform: uppercase; }
  .service-card__text { margin: 12px auto 0; width: 200px; font-size: 10px; line-height: 12.5px; }

  /* Contact */
  .contact-title {
    position: absolute; left: 0; top: 674px; width: 1200px; text-align: center;
    font-size: 32px; font-weight: 700; color: var(--rose); letter-spacing: 0.3px;
  }
  .contact-form { position: absolute; left: 376px; top: 763px; width: 452px; }
  .contact-form label { display: block; font-size: 12px; color: var(--ink); }
  .contact-form input {
    display: block; margin-top: 3px; width: 452px; height: 22px;
    border: 1px solid var(--field-border); background: var(--field-fill);
    padding: 0 4px; font-family: "Raleway", Arial, sans-serif; font-size: 11px;
  }
  .contact-form input::placeholder { color: var(--placeholder); font-style: italic; }
</style>
</head>
<body>
<div class="page">
  <header>
    <div class="brand">maren holt</div>
    <div class="help-line">Need a hand?Call me</div>
    <nav class="main-nav">
      <a href="#" style="left:116px">HOME</a>
      <a href="#" style="left:359px">MARKETING</a>
      <a href="#" style="left:600px">FINANCE</a>
      <a href="#" style="left:844px">BUSINESS COACH</a>
      <a href="#" style="left:1087px">CONTACT</a>
    </nav>
    <div class="accent-band"></div>
  </header>

  <section class="hero">
    <div class="hero-photo" role="img" aria-label="Desk photo: a hand on a laptop keyboard beside a spiral notebook and pen"></div>
    <h1 class="hero-title">Not all businesses can<br>afford the best...</h1>
    <a class="hero-button" href="#contact">GET IN TOUCH</a>
  </section>

  <div class="hero-fade"></div>

  <section class="services">
    <a class="service-card service-card--marketing" href="#">
      <div class="service-card__frame">
        <h2 class="service-card__title">Marketing</h2>
        <p class="service-card__text">Lorem ipsum dolor sit amet, consectetuer adipiscing elit. Aenean commodo ligula eget dolor.</p>
      </div>
    </a>
    <a class="service-card service-card--finance" href="#">
      <div class="service-card__frame">
        <h2 class="service-card__title">Finance</h2>
        <p class="service-card__text">Lorem ipsum dolor sit amet, consectetuer adipiscing elit. Aenean commodo ligula eget dolor.</p>
      </div>
    </a>
    <a class="service-card service-card--coach" href="#">
      <div class="service-card__frame">
        <h2 class="service-card__title">Business Coach</h2>
        <p class="service-card__text">Lorem ipsum dolor sit amet, consectetuer adipiscing elit. Aenean commodo ligula eget dolor.</p>
      </div>
    </a>
  </section>

  <section id="contact">
    <h2 class="contact-title">CONTACT</h2>
    <form class="contact-form">
      <label for="name">Name:</label>
      <input id="name" type="text" placeholder="Enter Name">
    </form>
  </section>
</div>
</body>
</html>
```